ebook front & back cover design: 'The Copper Lantern'

I am independent author writing under the pseudonym Reiko Matsudaira. I have already one novel published. I have written another historical novel, set in Japan in the 1950s. It is called 'The Copper Lantern'. The sub-title is 'A female spy uncovers secret weapons testing in cold-war Japan.' Japan in the 1950s was rocked by labour unrest and fear the Korean war would expand. The country was still governed by the US. The back cover copy is 'The Korean war has exploded. Neighbouring Japan is the staging post for US troops. Moscow encourages sabotage with its newly expanded spy network. There is a scramble to develop new weapons. Tungsten, a key component for shells, is scarce.

A communist sympathiser turned provocateur uncovers a secret weapons testing facility. The leaked news petrifies Washington and Tokyo. A talented counter intelligence officer is charged with tracking down the Soviet intelligence network. Is it too late?'

I want a design that communicates intrigue in the context of plot. The font for the author should be consistent with the first novel (attached). I expect the designs to use copyright free images/visuals, I will not pay for additional stock footage
Updates

Thanks to those who have already submitted initial designs. I have attached example visuals of Protest Art from Japan in the 1950s. I wish to make it explicitly clear that I do not own the copyright for these visuals and so they cannot be used. They are there only as reference material. All of the designs so far have used these visuals 'as is' Secondly there is an unexplained murder in the plot, a man is found drowned in suspicious circumstances, hence why one of the protest art visuals is a drowning man. Thirdly the spy is a Japanese women, a communist sympathiser turned provocateur. She is in her early 30s and is an art enthusiast. She is recruited by Russian intelligence at a protest art exhibition Fourthly please remember this is an e-book. Thumbnails are small on Brindlemart so the thumbnail visual must stand out clearly. You should use that as a 'test' before submitting ideas.

Target Market(s)

readers of historical fiction, spy stories. People who are interested in the cold war and Korea-Japan

Requirements
Must have
• This novel is historical fiction and a lot of time has been spent researching archives in English and Japanese for authenticity. There are references to protest art in the plot. Some actual examples attached below. The front cover should look like these in style, however I cannot use these exact images. My spy is a Japanese women, in her 30s, single, interested in art and literature. The front cover visual must have stand out impact when it appears as a thumbnail on Brindlemart
Nice to have
• (FYI Sakaiminato - photo attached) is where the weapons testing takes place. Not necessary to be on the cover, but to give you an idea of the area. It is remote Japan over 800KM from Tokyo
Should not have
• any stock footage/images that require additional costs

```html
<!DOCTYPE html>
<html lang="en">
<head>
<meta charset="utf-8">
<title>The Copper Lantern — Cover Spread</title>
<link href="https://fonts.googleapis.com/css2?family=Open+Sans:wght@400;600;700&family=Courier+Prime&family=Merienda:wght@700&display=swap" rel="stylesheet">
<style>
  :root {
    --stage: #000000;
    --ink-grey: #4a4a4a;
    --ink-dark: #2e2e2e;
    --accent-red: #d0402c;
    --circle-red: #b3261a;
    --paper: #f4f4f4;
    --paper-edge: #8a8a8a;
    --photo-dark: #3a3a3a;
    --photo-mid: #7a7a7a;
    --title-light: #e4e4e4;
    --white: #ffffff;
  }
  * { margin: 0; padding: 0; box-sizing: border-box; }
  html, body { width: 1200px; height: 955px; overflow: hidden; background: var(--stage); }
  .spread {
    position: absolute; left: 63px; top: 63px; width: 1078px; height: 784px;
    overflow: hidden; background: var(--paper);
  }

  /* back cover */
  .back-cover { position: absolute; left: 0; top: 0; width: 510px; height: 784px; overflow: hidden; }
  .back-photo {
    position: absolute; inset: 0;
    background: radial-gradient(ellipse at 62% 28%, #9a9a9a 0%, var(--photo-mid) 35%, var(--photo-dark) 85%);
  }
  .back-fade {
    position: absolute; right: 0; top: 0; width: 140px; height: 784px;
    background: linear-gradient(90deg, rgba(140,140,140,0) 0%, #a0a0a0 100%);
  }
  .red-disc {
    position: absolute; left: 42px; top: 274px; width: 432px; height: 432px;
    border-radius: 50%;
    background: radial-gradient(circle, var(--circle-red) 0%, var(--circle-red) 66%, rgba(179,38,26,0.8) 86%, rgba(179,38,26,0) 100%);
    opacity: 0.92;
  }
  .back-title {
    position: absolute; left: 50px; top: 232px; width: 200px; text-align: center;
    font-family: 'Open Sans', sans-serif; font-weight: 700; color: var(--title-light);
  }
  .back-title span { display: block; }
  .back-title .article { font-family: 'Merienda', cursive; font-size: 20px; line-height: 22px; color: #d8d8d8; }
  .back-title .title-line { font-size: 32px; line-height: 30px; }
  .blurb {
    position: absolute; left: 64px; top: 309px; width: 400px; text-align: center;
    font-family: 'Courier Prime', monospace; font-size: 16px; line-height: 18.8px; color: var(--white);
  }

  /* spine */
  .spine {
    position: absolute; left: 510px; top: 0; width: 56px; height: 784px;
    background: linear-gradient(90deg, #a4a4a4 0%, #cbcbcb 50%, #d6d6d6 100%);
  }
  .spine-text {
    position: absolute; left: 16px; top: 80px; writing-mode: vertical-rl;
    font-family: 'Open Sans', sans-serif; font-weight: 700; font-size: 20px; line-height: 24px;
    letter-spacing: 0.3em; color: var(--ink-grey); white-space: nowrap;
  }
  .spine-text .article { font-family: 'Merienda', cursive; color: var(--accent-red); letter-spacing: 0; font-size: 22px; margin-bottom: 6px; }
  .spine-text .accent { color: var(--accent-red); }
  .spine-text .spine-author { font-weight: 400; color: var(--ink-dark); margin-top: 26px; }

  /* front cover */
  .front {
    position: absolute; left: 566px; top: 0; width: 512px; height: 784px;
    background: radial-gradient(ellipse at 55% 52%, #ffffff 0%, #f6f6f6 45%, #cfcfcf 80%, var(--paper-edge) 100%);
  }
  .tagline {
    position: absolute; left: 0; top: 35px; width: 100%; text-align: center;
    font-family: 'Open Sans', sans-serif; font-weight: 600; font-size: 17.5px; line-height: 17px;
    color: var(--ink-dark);
  }
  .front-title { font-family: 'Open Sans', sans-serif; font-weight: 700; line-height: 1; }
  .front-title span { position: absolute; left: 0; width: 100%; text-align: center; }
  .front-title .article { top: 72px; font-family: 'Merienda', cursive; font-size: 46px; color: var(--accent-red); }
  .front-title .line-one { top: 121px; font-size: 68px; color: var(--ink-grey); }
  .front-title .line-two { top: 183px; font-size: 66px; color: var(--accent-red); }
  .hero-art {
    position: absolute; left: 187px; top: 270px; width: 222px; height: 429px;
    background: linear-gradient(180deg, #8a8a8a 0%, #5a5a5a 55%, #c88a86 85%, #e8e8e8 100%);
    border-radius: 40% 40% 6px 6px / 30% 30% 6px 6px;
    opacity: 0.85;
  }
  .front-author {
    position: absolute; left: 0; top: 725px; width: 100%; text-align: center;
    font-family: 'Open Sans', sans-serif; font-weight: 600; font-size: 26px; line-height: 1;
    letter-spacing: 0.35em; padding-left: 0.35em; color: var(--ink-dark);
  }
</style>
</head>
<body>
  <main class="spread">
    <section class="back-cover">
      <div class="back-photo" role="img" aria-label="Monochrome photograph of a woman in a kimono holding a lace fan, lace shadows across her face"></div>
      <div class="back-fade"></div>
      <div class="red-disc"></div>
      <h2 class="back-title">
        <span class="article">The</span>
        <span class="title-line">COPPER</span>
        <span class="title-line">LANTERN</span>
      </h2>
      <p class="blurb">This is<br>Layoutwise’s version<br>of Lorem Ipsum. Proin<br>gravida nibh vel velit auctor<br>aliquet. Aenean sollicitudin,<br>lorem quis bibendum auctor, nisi<br>elit consequat ipsum, nec sagittis<br>sem nibh id elit. Duis sed odio sit<br>amet nibh vulputate cursus a sit amet<br>mauris. Morbi accumsan ipsum velit. Nam<br>nec tellus a odio tincidunt auctor a<br>ornare odio. Sed non mauris vitae erat<br>consequat auctor eu in elit. Class<br>aptent taciti sociosqu ad litora<br>torquent per conubia nostra, per<br>inceptos himenaeos. Mauris in<br>erat. Nam nec tellus a odio<br>tincidunt auctor<br>a ornare odio.</p>
    </section>

    <section class="spine">
      <p class="spine-text"><span class="article">The</span> COPPER <span class="accent">LANTERN</span><span class="spine-author">REIKO MATSUDAIRA</span></p>
    </section>

    <section class="front">
      <p class="tagline">A FEMALE SPY UNCOVERS SECRET<br>WEAPONS TESTING IN COLD-WAR JAPAN</p>
      <h1 class="front-title">
        <span class="article">The</span>
        <span class="line-one">COPPER</span>
        <span class="line-two">LANTERN</span>
      </h1>
      <div class="hero-art" role="img" aria-label="Photograph of a grey artillery shell standing upright with a pink rose lying at its base"></div>
      <p class="front-author">REIKO MATSUDAIRA</p>
    </section>
  </main>
</body>
</html>
```